General Contractors need a new Crisp updated Card Design

We need a new business card design for our company of 25 years based in Toronto call Pollvarn Building Inc. : Our goal is to be the leading commercial contractors in Toronto by providing exceptional value to our clients. We work very hard to deliver professional, quality, service in conjunction with consistent price competitiveness to all of our clients on every single project.

Target Market(s)

Design & Build Clients

Industry/Entity Type

Construction Company

Contact Information for Business Card

Address:
18 West Marlow Field Road, Unit 17, Dunmore Vale, ON, K7T 2M9
Office: 905-218-6937

Pollvarns Logo
Employee Job Description
Employee Cell Phone #
Employee Email
www.pollvarn.example

Colors

Designer to choose colors to be used in the design.

Requirements
Must have
• Quote Company Saying:
• "Professional. Quality. Service."
Nice to have
• New Crisp up to date look. simple & fresh ( Not to Busy)
Should not have
• NO BLUE PRINTS ON THE BUSINESS CARDS

```html
<!DOCTYPE html>
<html lang="en">
<head>
<meta charset="utf-8">
<title>Pollvarn Building Inc. — Business Cards</title>
<link rel="stylesheet" href="https://fonts.googleapis.com/css2?family=Source+Sans+3:wght@400;600&display=swap">
<style>
  :root {
    --backdrop: #3a3430;
    --card: #141516;
    --card-edge: #1d1e20;
    --teal: #1f9184;
    --silver: #8e9194;
    --ink-light: #e6e6e6;
    --ink-soft: #b9bbbd;
    --rule: #cfd2d3;
  }
  * { box-sizing: border-box; margin: 0; padding: 0; }
  html, body { width: 1200px; height: 864px; overflow: hidden; }
  body {
    background: var(--backdrop);
    font-family: "Source Sans 3", "Myriad Pro", Arial, sans-serif;
    position: relative;
  }
  .card {
    position: absolute;
    left: 280px;
    width: 640px;
    height: 366px;
    background: var(--card);
    border: 1px solid var(--card-edge);
    box-shadow: 0 14px 30px rgba(0,0,0,.45);
  }
  .card--front { top: 44px; }
  .card--back { top: 454px; }

  /* Front */
  .brand {
    display: flex;
    align-items: center;
    gap: 12px;
    font-weight: 600;
    letter-spacing: .04em;
    text-transform: uppercase;
  }
  .brand__mark { width: 18px; height: 18px; }
  .card--front .brand {
    position: absolute;
    left: 118px;
    top: 118px;
    font-size: 36px;
    color: var(--silver);
  }
  .card--front .brand__mark { width: 30px; height: 30px; background: var(--silver); }
  .tagline {
    position: absolute;
    left: 162px;
    top: 214px;
    font-size: 17px;
    color: var(--ink-soft);
    letter-spacing: .01em;
  }

  /* Back */
  .card--back .brand {
    position: absolute;
    right: 40px;
    top: 48px;
    font-size: 24px;
    color: var(--teal);
  }
  .card--back .brand__mark { background: var(--teal); }
  .person {
    position: absolute;
    left: 40px;
    top: 110px;
  }
  .person__name {
    font-size: 19px;
    font-weight: 600;
    color: var(--teal);
    text-transform: uppercase;
    letter-spacing: .02em;
  }
  .person__role {
    font-size: 15px;
    color: var(--ink-light);
    text-transform: uppercase;
  }
  .rule {
    position: absolute;
    height: 1px;
    background: var(--rule);
  }
  .rule--top { left: 40px; right: 40px; top: 168px; }
  .rule--bottom { left: 340px; right: 40px; top: 262px; }
  .contacts {
    position: absolute;
    left: 40px;
    top: 182px;
    list-style: none;
    font-size: 16px;
    color: var(--ink-light);
    line-height: 24px;
  }
  .contacts li { display: flex; align-items: center; gap: 8px; }
  .contacts svg { width: 13px; height: 13px; fill: var(--teal); flex: none; }
  .address {
    position: absolute;
    right: 40px;
    top: 274px;
    text-align: right;
    font-style: normal;
    font-size: 17px;
    line-height: 22px;
    color: var(--ink-light);
  }
  .address__web { letter-spacing: .06em; }
</style>
</head>
<body>

<section class="card card--front" aria-label="Card front">
  <div class="brand"><span class="brand__mark"></span>Pollvarn Building Inc.</div>
  <p class="tagline">Professional. Quality. Service.</p>
</section>

<section class="card card--back" aria-label="Card back">
  <div class="brand"><span class="brand__mark"></span>Pollvarn Building Inc.</div>

  <div class="person">
    <p class="person__name">Mark Ellery</p>
    <p class="person__role">President</p>
  </div>

  <div class="rule rule--top"></div>

  <ul class="contacts">
    <li>
      <svg viewBox="0 0 16 16" aria-hidden="true"><path d="M3 1h3l1.5 4-2 1.2a9 9 0 0 0 4.3 4.3L11 8.5l4 1.5v3c0 1-1 2-2 2A13 13 0 0 1 1 3c0-1 1-2 2-2z"/></svg>
      905-218-6937
    </li>
    <li>
      <svg viewBox="0 0 16 16" aria-hidden="true"><path d="M4 0h8a1 1 0 0 1 1 1v14a1 1 0 0 1-1 1H4a1 1 0 0 1-1-1V1a1 1 0 0 1 1-1zm1 2v10h6V2zm3 11a1 1 0 1 0 0 2 1 1 0 0 0 0-2z"/></svg>
      905-218-4471
    </li>
    <li>
      <svg viewBox="0 0 16 16" aria-hidden="true"><path d="M0 3h16v10H0zm1.5 1.2L8 9l6.5-4.8V4h-13z"/></svg>
      info@pollvarn.example
    </li>
  </ul>

  <div class="rule rule--bottom"></div>

  <address class="address">
    18 West Marlow Field Road<br>
    Unit 17, Dunmore Vale, ON, K7T 2M9<br>
    <span class="address__web">www.pollvarn.example</span>
  </address>
</section>

</body>
</html>
```